Design an attractive wine label for Birch Vale Wines

we need a wine label design, we are an Australian wine exporting company'Birch Vale Wines'. We succeed several pallets in last few months and is going to launch our first container. So it’s time to start our own brands. we will have some wines display in China's shopping mall shelves, so we want to have a catchy label which can attract Chinese eyes immediately. other details you will see in the file i uploaded. The design should include a front and back label.

Target Market(s)

Birch Vale Wines are targeting middle class wine drinkers in 2nd-4th tier Chinese cities.

Colors

Designer to choose colors to be used in the design.

Requirements
Must have
• We’d like something that at first glance is Australian (element, style or color…) but subconsciously connects to the Chinese. Demeanor bearing in mind the demographics targeted across the ranges. We would expect the designs and naming to becoming more formalized as they rise to platinum.
Nice to have
• creative things come out
Should not have
• any dead related word or icon, no number '4' related word or icon, no skull related word or icon, kangaroo (see brand 'Crimson Wing')

```html
<!DOCTYPE html>
<html lang="en">
<head>
<meta charset="UTF-8">
<title>Lunar Cabernet Merlot – Front Label</title>
<link href="https://fonts.googleapis.com/css2?family=Josefin+Sans:wght@600&family=Montserrat:wght@500;700&family=Pinyon+Script&display=swap" rel="stylesheet">
<style>
  :root {
    --canvas-bg: #ffffff;
    --label-light: #f1f1ee;
    --label-mid: #d8d8d5;
    --ink-dark: #2b2b2b;
    --band-black: #101010;
    --band-edge: #1a1a1a;
    --gold: #c9a24a;
    --wine-red: #d01f2e;
    --rule-grey: #5a5a5a;
    --petal-red: #d8283a;
    --petal-pink: #f3c4c8;
  }
  * { margin: 0; padding: 0; box-sizing: border-box; }
  html, body {
    width: 906px;
    height: 1200px;
    overflow: hidden;
    background: var(--canvas-bg);
  }
  .canvas {
    position: relative;
    width: 906px;
    height: 1200px;
  }
  .front-label {
    position: absolute;
    left: 108px;
    top: 128px;
    width: 690px;
    height: 712px;
    overflow: hidden;
    background: linear-gradient(90deg, var(--label-light) 0%, #e6e6e3 30%, var(--label-mid) 55%, #e9e9e7 80%, var(--label-light) 100%);
  }
  .petal-motif {
    position: absolute;
    left: 276px;
    top: 0;
    width: 414px;
    height: 360px;
    border-radius: 100% 0 0 100% / 50% 0 0 50%;
    background: radial-gradient(ellipse 100% 70% at 100% 50%, #fbeff0 0%, var(--petal-pink) 45%, #e4727d 75%, var(--petal-red) 100%);
  }
  .vintage {
    position: absolute;
    top: 458px;
    width: 100%;
    text-align: center;
    font-family: 'Montserrat', sans-serif;
    font-weight: 500;
    font-size: 24px;
    letter-spacing: 6px;
    color: var(--ink-dark);
  }
  .region {
    position: absolute;
    top: 542px;
    width: 100%;
    text-align: center;
    font-family: 'Pinyon Script', cursive;
    font-size: 46px;
    color: var(--ink-dark);
  }
  .name-band {
    position: absolute;
    left: 151px;
    top: 840px;
    width: 610px;
    height: 163px;
    background: linear-gradient(180deg, var(--band-edge) 0%, var(--band-black) 50%, var(--band-edge) 100%);
  }
  .wine-name {
    position: absolute;
    top: 44px;
    width: 100%;
    text-align: center;
    font-family: 'Josefin Sans', sans-serif;
    font-weight: 600;
    font-size: 48px;
    line-height: 48px;
    letter-spacing: 9px;
    color: var(--gold);
  }
  .varietal-row {
    position: absolute;
    top: 118px;
    left: 22px;
    right: 22px;
    display: flex;
    align-items: center;
    gap: 18px;
  }
  .varietal-rule {
    flex: 1;
    height: 2px;
    background: var(--rule-grey);
  }
  .varietal {
    font-family: 'Montserrat', sans-serif;
    font-weight: 700;
    font-size: 18px;
    line-height: 24px;
    letter-spacing: 2px;
    color: var(--wine-red);
    white-space: nowrap;
  }
</style>
</head>
<body>
  <main class="canvas">
    <section class="front-label">
      <div class="petal-motif" role="img" aria-label="Red line-drawn flower petals radiating from the right edge"></div>
      <p class="vintage">2007</p>
      <p class="region">Western Australia Wine</p>
    </section>
    <section class="name-band">
      <h1 class="wine-name">LUNAR</h1>
      <div class="varietal-row">
        <span class="varietal-rule"></span>
        <span class="varietal">CABERNET MARLOT</span>
        <span class="varietal-rule"></span>
      </div>
    </section>
  </main>
</body>
</html>
```